Business Card for Technology Startup

Design a 2-sided business card using the logo provided. We are a digital healthcare platform that provides a mobile app and web UI that helps caregivers, families, and doctors share information and provide better patient outcomes. We use AI and machine learning to help guide patients through their day-to-day life. The final design should communicate stability, peace, comfort, but also align with the image of an AI-driven technology startup.

I'd like the deliverable to by a Photoshop PSD file (with layers) that I can work with in pixlr.com. Should contain the following editable layers:
Name (ex. John Doe)
Title (ex. Founder / CEO)
Email (ex. info@brenvaxa.ai)
Phone (ex. (555) 014-2280)
Website (ex. https://brenvaxa.ai)

```html
<!DOCTYPE html>
<html lang="en">
<head>
<meta charset="utf-8">
<title>Brenvaxa Business Card</title>
<link rel="stylesheet" href="https://fonts.googleapis.com/css2?family=Lexend:wght@400;500;600&display=swap">
<style>
  :root {
    --backdrop: #b4b4b4;
    --card: #000000;
    --accent: #10d4f0;
    --accent-deep: #0aa8e6;
    --ink: #ffffff;
  }
  * { margin: 0; padding: 0; box-sizing: border-box; }
  html, body { width: 1200px; height: 900px; overflow: hidden; }
  body {
    background: var(--backdrop);
    font-family: "Lexend", "Helvetica Neue", Arial, sans-serif;
    color: var(--ink);
    position: relative;
  }
  .card {
    position: absolute;
    left: 280px;
    width: 640px;
    height: 366px;
    background: var(--card);
    border-radius: 4px;
    box-shadow: 0 10px 28px rgba(0,0,0,0.28);
    overflow: hidden;
  }
  .card--front { top: 42px; }
  .card--back { top: 450px; }

  .front-mark {
    position: absolute;
    inset: 0;
    display: flex;
    align-items: center;
    justify-content: center;
    gap: 18px;
  }
  .front-mark__dot {
    width: 34px; height: 34px; border-radius: 50%;
    background: var(--accent);
  }
  .front-mark__name {
    font-size: 44px; font-weight: 600; color: var(--accent);
    letter-spacing: 0.5px;
  }

  .brand {
    position: absolute; left: 48px; top: 46px;
    display: flex; align-items: center; gap: 12px;
  }
  .brand__dot { width: 18px; height: 18px; border-radius: 50%; background: var(--accent); }
  .brand__name { font-size: 34px; font-weight: 600; color: var(--ink); letter-spacing: 0.3px; }

  .person { position: absolute; left: 76px; top: 128px; }
  .person__name { font-size: 36px; font-weight: 500; color: var(--accent); line-height: 1.1; }
  .person__title { font-size: 17px; font-weight: 400; margin-top: 4px; }

  .contacts {
    position: absolute; left: 86px; top: 232px;
    list-style: none; display: flex; flex-direction: column; gap: 12px;
  }
  .contacts__item { display: flex; align-items: center; gap: 12px; font-size: 16px; white-space: nowrap; }
  .contacts__icon { width: 18px; height: 18px; flex: none; }

  .back-decor {
    position: absolute; right: 70px; top: 70px;
    width: 210px; height: 210px; border-radius: 50%;
    background: linear-gradient(135deg, var(--accent), var(--accent-deep));
  }
</style>
</head>
<body>
  <section class="card card--front" aria-label="Card front">
    <div class="front-mark">
      <span class="front-mark__dot"></span>
      <span class="front-mark__name">brenvaxa</span>
    </div>
  </section>

  <section class="card card--back" aria-label="Card back">
    <div class="brand">
      <span class="brand__dot"></span>
      <span class="brand__name">brenvaxa</span>
    </div>

    <div class="person">
      <p class="person__name">John Doe</p>
      <p class="person__title">Founder / CEO</p>
    </div>

    <ul class="contacts">
      <li class="contacts__item">
        <svg class="contacts__icon" viewBox="0 0 20 20" aria-hidden="true">
          <rect x="1" y="4" width="18" height="12" rx="1" fill="var(--accent)"/>
          <path d="M1.5 4.5 L10 11 L18.5 4.5" fill="none" stroke="#000" stroke-width="1.4"/>
        </svg>
        <span>info@brenvaxa.ai</span>
      </li>
      <li class="contacts__item">
        <svg class="contacts__icon" viewBox="0 0 20 20" aria-hidden="true">
          <path d="M5 2 L8 2 L9 6 L7 7.5 C8 10 10 12 12.5 13 L14 11 L18 12 L18 15 C18 16.5 17 17.5 15.5 17.5 C8.5 17 3 11.5 2.5 4.5 C2.5 3 3.5 2 5 2 Z" fill="var(--accent)"/>
        </svg>
        <span>(555) 014-2280</span>
      </li>
      <li class="contacts__item">
        <svg class="contacts__icon" viewBox="0 0 20 20" aria-hidden="true">
          <circle cx="10" cy="10" r="8.5" fill="none" stroke="var(--accent)" stroke-width="1.6"/>
          <ellipse cx="10" cy="10" rx="3.6" ry="8.5" fill="none" stroke="var(--accent)" stroke-width="1.4"/>
          <path d="M1.5 10 H18.5 M3 5.8 H17 M3 14.2 H17" stroke="var(--accent)" stroke-width="1.3"/>
        </svg>
        <span>https://brenvaxa.ai</span>
      </li>
    </ul>

    <div class="back-decor" aria-hidden="true"></div>
  </section>
</body>
</html>
```